A5 spiral bound, full colour, baby massage booklet

We need full design of an A5 instruction booklet on baby massage to help parents remember what they have learned at baby massage classes. The booklet will be bi-lingual with text in english and mandarin. Designs need to be in line with the look of the Cradle Touch Guidance Network website (cradletouchhub.net.au) and other Cradle Touch Guidance products.
To give an indication of length, our current manual (which is in need of refreshing and updating being monotone and in English only is 30 pages.)
We need a print ready file or folder that can be provided to a printer to produce the final product.

Target Market(s)

Parents wanting to learn baby massage

Industry/Entity Type

Baby massage

Colors
6B429C
8869AF
B7A5CE
E3DAEB
F3F0F8

Requirements
Nice to have
• Logo, images of massage techniques coupled with English and Mandarin instructions

```html
<!DOCTYPE html>
<html lang="en">
<head>
<meta charset="utf-8">
<title>Baby Massage – Booklet Pages</title>
<link href="https://fonts.googleapis.com/css2?family=Poppins:wght@300;400;500;600;700&display=swap" rel="stylesheet">
<style>
:root{
  --backdrop:#4b4b4b;
  --plum:#9c2a8c;
  --plum-soft:#c77dbb;
  --paper:#efefef;
  --cover:#ffffff;
  --ink:#2a2a2a;
  --body:#3d3d3d;
  --slate:#5a5a5c;
  --rule:#5d5d60;
}
*{box-sizing:border-box;margin:0;padding:0}
html,body{width:1074px;height:1200px;overflow:hidden;background:var(--backdrop)}
body{font-family:'Poppins',sans-serif;color:var(--body);position:relative}
.page{position:absolute;background:var(--paper);overflow:hidden}
.page.cover{background:var(--cover)}
.band{position:absolute;left:0;top:0;right:0;height:20px;background:var(--plum);color:#fff}
.band .brand{position:absolute;left:20px;top:5px;display:flex;align-items:center;gap:3px;font-size:3px;line-height:1.1;width:40px}
.band .brand i{display:block;width:6px;height:6px;border-radius:50%;border:.6px solid #fff;flex:none}
.band .run{position:absolute;right:20px;top:6px;text-align:right;font-size:3.6px;line-height:1.3}
.band .run b{font-weight:600;display:block}
.title{position:absolute;left:20px;top:34px;color:var(--plum);font-weight:600;font-size:8.6px}
.foot{position:absolute;left:0;right:20px;bottom:21px;height:1.3px;background:var(--rule)}
.foot-note{position:absolute;left:20px;bottom:15px;font-size:3.6px;color:var(--plum)}
.folio{position:absolute;right:20px;bottom:12px;width:7px;height:9px;background:var(--rule);color:#fff;font-size:3.4px;text-align:center;line-height:9px}
.txt{position:absolute;font-size:4.6px;line-height:1.3;color:var(--body)}
.txt p{margin-bottom:1px}
.txt.just p{text-align:justify}
.sub{color:var(--plum);font-size:6.4px;font-weight:400;margin:4px 0 1px}
.sub.sm{font-size:5px}
.photo{position:absolute}
.grid2{display:grid;grid-template-columns:1fr 1fr;column-gap:5px;row-gap:3px;margin-top:2px}
/* covers */
.cover-title{position:absolute;left:22px;font-size:21px;font-weight:700;letter-spacing:.2px;line-height:1}
.cover-sub{position:absolute;left:23px;font-size:5.6px;color:var(--slate)}
/* toc */
.toc{position:absolute;left:20px;right:35px;top:80px;font-size:5.6px;color:var(--ink)}
.toc li{list-style:none;display:flex;align-items:baseline;height:14.4px}
.toc li span.dots{flex:1;border-bottom:.6px dotted #555;margin:0 1px}
/* checklist */
.check{list-style:none}
.check li{display:flex;gap:5px;margin-bottom:5px}
.check li svg{flex:none;width:5px;height:5px;margin-top:.5px}
</style>
</head>
<body>

<!-- Front cover -->
<section class="page cover" style="left:117px;top:53px;width:247px;height:353px">
  <div style="position:absolute;left:47px;top:74px;width:54px;height:44px;background:var(--plum);border-radius:5px"></div>
  <div class="photo" role="img" aria-label="Parent's hands massaging a smiling baby's tummy" style="left:104px;top:43px;width:102px;height:74px;border-radius:0 6px 0 0;background:linear-gradient(135deg,#b9d3e4,#e9dcd2 60%,#f3ece8)"></div>
  <div style="position:absolute;left:0;top:120px;width:101px;height:85px;background:var(--slate);border-radius:0 0 8px 0"></div>
  <div class="photo" role="img" aria-label="Close-up of hands holding a baby's feet, pink tint" style="left:104px;top:120px;width:102px;height:76px;border-radius:0 6px 0 6px;background:linear-gradient(135deg,#c67fb8,#d9a3cd 55%,#b95fa6)"></div>
  <h1 class="cover-title" style="top:221px;color:var(--plum)">BABY MASSAGE</h1>
  <p class="cover-sub" style="top:243px">Your Step-by-Step Guide for Massage Time</p>
  <div style="position:absolute;left:150px;top:318px;font-size:3.6px;line-height:1.3;color:var(--slate)">
    <span style="color:var(--plum)">Produced by the</span><br>Cradle Touch Guidance Network<br>www.cradletouch-ctgn.com.au
  </div>
</section>

<!-- Title page -->
<section class="page cover" style="left:388px;top:50px;width:247px;height:353px">
  <h1 class="cover-title" style="top:223px;color:var(--ink)">BABY MASSAGE</h1>
  <p class="cover-sub" style="top:244px">Your Step-by-Step Guide for Massage Time</p>
</section>

<!-- Forward -->
<section class="page" style="left:689px;top:50px;width:245px;height:351px">
  <header class="band"><div class="brand"><i></i>Cradle Touch Guidance Network</div><div class="run"><b>BABY MASSAGE</b>Your Step-by-Step Guide for Massage Time</div></header>
  <h2 class="title">Forward</h2>
  <div class="photo" role="img" aria-label="Black and white portrait of the founder" style="left:20px;top:70px;width:70px;height:86px;border-radius:8px 0 0 0;background:linear-gradient(160deg,#d8d8d8,#8c8c8c)"></div>
  <div style="position:absolute;left:91px;top:78px;width:1.2px;height:78px;background:var(--plum)"></div>
  <h3 class="sub" style="position:absolute;left:98px;top:96px;font-size:7.6px;margin:0">The Importance of Touch</h3>
  <div class="txt" style="left:98px;top:119px;width:127px"><p>To infants and children, touch is a basic physical and emotional need, as vital as food. It has been well documented that infants and children deprived of physical contact suffer from negative signs and symptoms, both physically and psychologically.</p></div>
  <div class="txt just" style="left:20px;top:159px;width:205px">
    <p>Massage provides quality time between you and your child, enhancing the bonding process, while offering other physical and emotional benefits. Provide only as much massage as your child is willing to receive and try to offer massage each day. Regardless of the amount of time you can spare, if your child is willing, some massage is better than no massage at all.</p>
    <p>Enjoy this experience with your child, the benefits will certainly be shared by both of you.</p>
    <p>Should you experience any difficulty in practicing the techniques to follow, or would like further clarification on any sequence, please do not hesitate to contact a qualified instructor for assistance, or contact the Information Service directly.</p>
  </div>
  <div role="img" aria-label="Handwritten signature" style="position:absolute;left:20px;top:248px;width:38px;height:10px;background:#e2e2e2"></div>
  <div class="txt" style="left:20px;top:261px;font-size:4.8px;color:#777">Clara Whitfield<br>Founder, CTGN</div>
  <div class="foot"></div><div class="foot-note">©2008 Cradle Touch Guidance Network</div><div class="folio">1</div>
</section>

<!-- Table of contents -->
<section class="page" style="left:109px;top:448px;width:240px;height:343px">
  <header class="band"><div class="brand"><i></i>Cradle Touch Guidance Network</div><div class="run"><b>BABY MASSAGE</b>Your Step-by-Step Guide for Massage Time</div></header>
  <h2 class="title">Table of Contents</h2>
  <ul class="toc">
    <li>Forward<span class="dots"></span>1</li>
    <li>Table of Contents<span class="dots"></span>2</li>
    <li>Benefits of infant massage<span class="dots"></span>3</li>
    <li>Contraindication<span class="dots"></span>4</li>
    <li>What oil to use<span class="dots"></span>5</li>
    <li>Safe massage<span class="dots"></span>6</li>
    <li>Checklist massage<span class="dots"></span>7</li>
    <li>Beginning the sequence<span class="dots"></span>8</li>
    <li>'Yes' And 'No' Response Cues for Massage Time<span class="dots"></span>9</li>
    <li>Massage for wind<span class="dots"></span>24</li>
    <li>Exercises<span class="dots"></span>27</li>
    <li>Massage for the older child<span class="dots"></span>29</li>
  </ul>
  <div class="foot"></div><div class="foot-note">©2008 Cradle Touch Guidance Network</div><div class="folio">2</div>
</section>

<!-- Benefits -->
<section class="page" style="left:404px;top:448px;width:233px;height:333px">
  <header class="band"><div class="brand"><i></i>Cradle Touch Guidance Network</div><div class="run"><b>BABY MASSAGE</b>Your Step-by-Step Guide for Massage Time</div></header>
  <h2 class="title" style="top:32px">Benefits of Infant Massage</h2>
  <div class="txt just" style="left:20px;top:50px;width:193px">
    <p>Baby massage can provide so many wonderful benefits, not only to infants, but also to the family unit.</p>
    <h3 class="sub">Relief of discomfort</h3>
    <p>Massage releases endorphins and can assist in relieving discomfort associated with teething, chest and sinus congestion, colic and reflux.</p>
    <h3 class="sub">Sleep</h3>
    <p>Most babies sleep for longer periods following massage and have longer periods of deep sleep.</p>
    <h3 class="sub">Teaches children that they are in charge of their own body</h3>
    <p>CTGN teaches parents to interpret an infant's body language in regards to massage. If you interpret a 'no cue' from your baby, respond appropriately by either not continuing or not beginning the massage. By respecting a child's rejection of touch, you are teaching your baby that they deserve respect when it comes to making decisions about who touches their body and that it is ok to say no if you don't want to be touched.</p>
    <h3 class="sub sm">Massage also...</h3>
    <div class="grid2">
      <span>Speeds brain and nervous system development</span><span>Assists with the development of co-ordination and balance. Increases body awareness</span>
      <span>Aids relaxation</span><span>Strengthens the immune system</span>
      <span>Helps tone muscles and aids growth</span><span>Enhances the bonding process</span>
      <span>Aids digestion and deepens respiration</span><span>Can help older siblings bond with their new brother or sister</span>
      <span>Teaches infants that touch is a form of expression</span><span></span>
    </div>
    <h3 class="sub">Benefits for parents</h3>
    <p>Parents and Grandparents also benefit from providing massage. Research has shown that adults who provide massage to infants experience less anxiety, fewer depressive symptoms, improved mood, decreased stressed levels and improved self-esteem.</p>
  </div>
  <div class="foot"></div><div class="foot-note">©2008 Cradle Touch Guidance Network</div><div class="folio">3</div>
</section>

<!-- Contraindications -->
<section class="page" style="left:696px;top:445px;width:238px;height:340px">
  <header class="band"><div class="brand"><i></i>Cradle Touch Guidance Network</div><div class="run"><b>BABY MASSAGE</b>Your Step-by-Step Guide for Massage Time</div></header>
  <h2 class="title" style="top:30px">Contraindications</h2>
  <div class="txt just" style="left:20px;top:47px;width:198px">
    <h3 class="sub">When it is best not to massage?</h3>
    <p>Contraindications are situations in which massage should be avoided. If you are ever unsure of whether you should avoid massage or not please contact your health care provider or your infant massage instructor.</p>
    <div class="grid2" style="row-gap:4px;margin:4px 2px">
      <span>Bleeding</span><span>No massage over an unhealed navel</span>
      <span>Open or weeping</span><span>Burns, including sun burn</span>
      <span>Wounds</span><span>Undiagnosed lumps</span>
      <span>Infected skin irritations</span><span>No abdominal massage if your baby has hiccups or has just been fed</span>
      <span>Fractures or other acute injuries</span><span></span>
    </div>
    <h3 class="sub">When it is best not to massage?</h3>
    <p>Try to use a pure cold pressed fruit, nut, vegetable or seed oil which is free from pesticides and is organic.</p>
    <p>Pure cold pressed oil is easily absorbed by the skin as opposed to mineral oil, which tends to leave a greasy film over the skin's surface. Because cold pressed oils are absorbed so well, it is important that they are free from pesticides as there is a concern of pesticides being absorbed into the body's systems with the oil.</p>
    <p>Infants tend to put their hands, or feet in their mouth during massage, and for this reason, it is important that you are happy for your baby to ingest the oil you are going to use for massage time. This recommendation does not apply in reverse, i.e. just because an oil is edible, does not mean it is necessarily suitable for infant massage. Take olive oil for example. This can be purchased as pure, cold pressed, organic oil, is a fruit oil, and is of course edible. Its texture however, is too thick and it will not be absorbed sufficiently by the skin.</p>
  </div>
  <div class="foot"></div><div class="foot-note">©2008 Cradle Touch Guidance Network</div><div class="folio">4</div>
</section>

<!-- What oil to use -->
<section class="page" style="left:124px;top:824px;width:233px;height:334px">
  <header class="band"><div class="brand"><i></i>Cradle Touch Guidance Network</div><div class="run"><b>BABY MASSAGE</b>Your Step-by-Step Guide for Massage Time</div></header>
  <h2 class="title" style="top:28px">What Oil to Use</h2>
  <div class="photo" role="img" aria-label="Black and white still life of an oil bottle and cream jar with daisies" style="left:20px;top:49px;width:193px;height:86px;background:linear-gradient(180deg,#f4f4f4,#cfcfcf 70%,#e6e6e6)"></div>
  <div class="txt just" style="left:20px;top:140px;width:193px">
    <p><em>Whatever oil you use for massage. You need to be happy for your baby to ingest.</em> This recommendation does not apply in reverse, i.e. just because an oil is edible, does not necessarily make it suitable for massage.</p>
    <h3 class="sub">Nut allergies</h3>
    <p>Caution should be taken if you are aware or concerned regarding a family history of nut allergies. In these situations it is recommended to avoid using nut oils. In any case, peanut oil is never recommended for use in infant massage.</p>
    <h3 class="sub">Sesame oil</h3>
    <p>Sesame oil has a wonderful texture for massage. It is easily absorbed when purchased as a cold pressed product (i.e. not cooking sesame oil found at the supermarket). Sesame oil is available at a reasonable price, even when purchased as an organic product.</p>
    <p>Sesame oil contains a range of antioxidants some of which help to naturally preserve the oil. If stored properly, sesame oil is not likely to go rancid. It is also high in vitamins A, B and E in addition to containing iron, calcium and other beneficial minerals.</p>
    <p>This oil is immensely popular in India where its use in massage, for many, is a part of every day life. Its chemical structure gives it the unique ability to penetrate the skin easily.</p>
    <p>Sesame oil naturally comprises of up to 40% linoleic acid which is used in the production of many soaps because of its antibacterial properties.</p>
  </div>
  <div class="foot"></div><div class="foot-note">©2008 Cradle Touch Guidance Network</div><div class="folio">5</div>
</section>

<!-- Safe positioning -->
<section class="page" style="left:407px;top:824px;width:237px;height:340px">
  <header class="band"><div class="brand"><i></i>Cradle Touch Guidance Network</div><div class="run"><b>BABY MASSAGE</b>Your Step-by-Step Guide for Massage Time</div></header>
  <h2 class="title" style="top:28px">Safe Positioning for Infant</h2>
  <div class="photo" role="img" aria-label="Newborn lying on a parent's thighs, black and white" style="left:20px;top:50px;width:77px;height:42px;background:linear-gradient(135deg,#cfcfcf,#7d7d7d)"></div>
  <div style="position:absolute;left:48px;top:92px;width:26px;height:9px;background:var(--plum)"></div>
  <div class="photo" role="img" aria-label="Baby lying on a towel on the floor, black and white" style="left:20px;top:101px;width:77px;height:57px;background:linear-gradient(135deg,#bdbdbd,#6f6f6f)"></div>
  <div style="position:absolute;left:48px;top:158px;width:26px;height:9px;background:var(--plum)"></div>
  <div class="photo" role="img" aria-label="Baby sitting up supported by a parent, black and white" style="left:20px;top:167px;width:77px;height:116px;background:linear-gradient(160deg,#d4d4d4,#727272)"></div>
  <div class="txt just" style="left:102px;top:50px;width:115px;font-size:4.5px">
    <h3 class="sub sm" style="margin-top:0">Newborns</h3>
    <p>Leaning against a wall or sofa, sit on the floor with your knees bent. Newborn infants can comfortably lie on your thighs, head resting on your knees. This is a wonderful position for new babies as it provides a good distance between you for eye contact.</p>
    <h3 class="sub sm" style="margin-top:5px">Lying On The Floor</h3>
    <p>It is best to massage your baby on the floor, as opposed to a change table. During massage time, your baby's skin will be slippery while covered with oil, meaning you could slip when you pick Baby up. Lay your baby on a change mat and a towel or blanket in front of you. To make sure you are comfortable during massage time sit on a cushion in front of a wall or sofa to support your back.</p>
    <h3 class="sub sm" style="margin-top:5px">Sitting Up For Massage Time</h3>
    <p>Once your baby can support herself a little she can sit in front of you for massage time. You can place some of their favourite toys in front of them to keep them entertained or even sit in front of a full-length mirror so they can watch themselves throughout their massage. Sitting in front of a mirror for massage is fantastic for increasing your baby's body awareness. She will both see and feel you massaging her arm as you say "arm", and feel and see you massaging her leg as you say "leg", and so on.</p>
    <h3 class="sub sm" style="margin-top:5px">Rolling Over</h3>
    <p>If your baby is happy to receive massage while rolling around back and forth in front of you, massage the area that is available each time they roll. Massage on the floor and never restrict his/her movement.</p>
  </div>
  <div class="foot"></div><div class="foot-note">©2008 Cradle Touch Guidance Network</div><div class="folio">6</div>
</section>

<!-- Checklist -->
<section class="page" style="left:699px;top:824px;width:238px;height:340px">
  <header class="band"><div class="brand"><i></i>Cradle Touch Guidance Network</div><div class="run"><b>BABY MASSAGE</b>Your Step-by-Step Guide for Massage Time</div></header>
  <h2 class="title" style="top:28px">Checklist for Massage</h2>
  <div class="photo" role="img" aria-label="Black and white photo of a parent writing a checklist beside baby items" style="left:20px;top:50px;width:196px;height:124px;background:linear-gradient(135deg,#8f8f8f,#d9d9d9 55%,#a9a9a9)"></div>
  <div class="txt" style="left:20px;top:180px;width:196px">
    <h3 class="sub" style="margin-top:0;margin-bottom:4px">Checklist for Massage Time</h3>
    <ul class="check">
      <li><svg viewBox="0 0 10 10"><rect x=".5" y=".5" width="9" height="9" fill="#fff" stroke="#8c8c8c"/><path d="M2 5l2 2 4-5" fill="none" stroke="#9c2a8c" stroke-width="1.4"/></svg><span>Is it a good time for you? Are you relaxed?</span></li>
      <li><svg viewBox="0 0 10 10"><rect x=".5" y=".5" width="9" height="9" fill="#fff" stroke="#8c8c8c"/><path d="M2 5l2 2 4-5" fill="none" stroke="#9c2a8c" stroke-width="1.4"/></svg><span>Is it a good time for your child?</span></li>
      <li><svg viewBox="0 0 10 10"><rect x=".5" y=".5" width="9" height="9" fill="#fff" stroke="#8c8c8c"/><path d="M2 5l2 2 4-5" fill="none" stroke="#9c2a8c" stroke-width="1.4"/></svg><span>Get the oil, towel, music etc, ready for your massage time.</span></li>
      <li><svg viewBox="0 0 10 10"><rect x=".5" y=".5" width="9" height="9" fill="#fff" stroke="#8c8c8c"/><path d="M2 5l2 2 4-5" fill="none" stroke="#9c2a8c" stroke-width="1.4"/></svg><span>Remove any jewellery that may scratch your baby during massage (including rings, watches and bracelets).</span></li>
      <li><svg viewBox="0 0 10 10"><rect x=".5" y=".5" width="9" height="9" fill="#fff" stroke="#8c8c8c"/><path d="M2 5l2 2 4-5" fill="none" stroke="#9c2a8c" stroke-width="1.4"/></svg><span>Check the light in the room. When you lie your baby down will there be glare, or bright light in his eyes?</span></li>
      <li><svg viewBox="0 0 10 10"><rect x=".5" y=".5" width="9" height="9" fill="#fff" stroke="#8c8c8c"/><path d="M2 5l2 2 4-5" fill="none" stroke="#9c2a8c" stroke-width="1.4"/></svg><span>Try to make sure your hands are nice and warm. Warm them briefly in front of a heater or under some warm water just before you're ready to start.</span></li>
    </ul>
  </div>
  <div class="foot"></div><div class="foot-note">©2008 Cradle Touch Guidance Network</div><div class="folio">7</div>
</section>

</body>
</html>
```